Business Card Design Project 4 Construction Business

I am after a creative, but sleek and simple/ clean business card design. This design will form the basis of future items and might include a logo or simply a creative way to lay out the text of my company name 'kestrel ventures'
I like the simplicity of black and white however I would also be happy to see a splash of colour introduced somehow to give the text some interest and make it stand out.
I would like a double sided card.
I am young (ish!) and professional, offering construction and project management services, what I don't want is the traditional builders type card featuring a cheesy hammer/ saw image etc.
As the company name, kestrel ventures, suggests, we focus on working closely and collaboratively together, in synergy with all stakeholders involved in the projects that we undertake
Construction

```html
<!DOCTYPE html>
<html lang="en">
<head>
<meta charset="utf-8">
<title>Kestrel Ventures – Business Card</title>
<link rel="stylesheet" href="https://fonts.googleapis.com/css2?family=Quicksand:wght@400;500&display=swap">
<style>
  :root {
    --backdrop: #141414;
    --card-dark: #1f2020;
    --card-band: #333634;
    --brand-red: #a1030a;
    --brand-red-deep: #6e0a0d;
    --paper: #ffffff;
    --ink: #1b1b1b;
    --contact-text: #ececec;
  }
  * { margin: 0; padding: 0; box-sizing: border-box; }
  html, body {
    width: 1200px;
    height: 900px;
    overflow: hidden;
    background: var(--backdrop);
    font-family: "Quicksand", sans-serif;
  }
  .canvas {
    position: relative;
    width: 1200px;
    height: 900px;
  }
  .card {
    position: absolute;
    width: 540px;
    height: 290px;
    overflow: hidden;
    background: var(--card-dark);
    box-shadow: 0 6px 18px rgba(0, 0, 0, 0.6);
  }
  .card-art {
    position: absolute;
    inset: 0;
    width: 100%;
    height: 100%;
  }
  .card-front { left: 115px; top: 125px; }
  .card-back  { left: 200px; top: 455px; }

  .brand-name {
    position: absolute;
    color: var(--brand-red);
    font-weight: 400;
    letter-spacing: 0.5px;
    white-space: nowrap;
  }
  .card-front .brand-name {
    left: 16px;
    bottom: 22px;
    font-size: 40px;
  }
  .standalone-brand {
    left: 748px;
    top: 284px;
    font-size: 42px;
  }

  .contact-list {
    position: absolute;
    right: 18px;
    top: 42px;
    list-style: none;
    text-align: right;
    color: var(--contact-text);
    font-size: 14.5px;
    line-height: 21px;
    font-weight: 400;
  }
  .contact-list .split-line {
    display: flex;
    justify-content: flex-end;
    gap: 40px;
  }
  .holder {
    position: absolute;
    left: 22px;
    bottom: 28px;
  }
  .holder-name {
    color: var(--ink);
    font-size: 26px;
    font-weight: 500;
    line-height: 30px;
  }
  .holder-role {
    color: var(--brand-red);
    font-size: 14px;
    font-weight: 500;
    letter-spacing: 0.5px;
    margin-left: 48px;
  }
</style>
</head>
<body>
<main class="canvas">

  <section class="card card-front" aria-label="Card front">
    <svg class="card-art" viewBox="0 0 540 290" aria-hidden="true">
      <defs>
        <linearGradient id="front-red" x1="0" y1="0" x2="1" y2="1">
          <stop offset="0" stop-color="#b0040b"/>
          <stop offset="1" stop-color="#5a0b0d"/>
        </linearGradient>
      </defs>
      <polygon class="accent-band" points="40,0 110,0 525,290 455,290" fill="var(--card-band)"/>
      <polygon class="accent-field" points="110,0 540,0 540,290 525,290" fill="url(#front-red)"/>
    </svg>
    <p class="brand-name">Kestrel Ventures</p>
  </section>

  <section class="card card-back" aria-label="Card back">
    <svg class="card-art" viewBox="0 0 540 290" aria-hidden="true">
      <defs>
        <linearGradient id="back-dark" x1="0" y1="0" x2="1" y2="1">
          <stop offset="0" stop-color="#2a2c2b"/>
          <stop offset="1" stop-color="#1c1d1d"/>
        </linearGradient>
      </defs>
      <rect width="540" height="290" fill="url(#back-dark)"/>
      <polygon class="accent-band" points="0,0 40,0 410,290 0,290" fill="var(--brand-red)"/>
      <polygon class="name-field" points="0,70 330,290 0,290" fill="var(--paper)"/>
    </svg>
    <ul class="contact-list">
      <li class="split-line"><span>www.kestrelventuresgroup.com.au</span><span>p: 0491 570 118</span></li>
      <li>e: oliver@kestrelventuresgroup.com.au</li>
      <li>a: 18 Corella Ave Lindfield NSW 2070</li>
    </ul>
    <div class="holder">
      <p class="holder-name">Oliver Brandt</p>
      <p class="holder-role">DIRECTOR</p>
    </div>
  </section>

  <p class="brand-name standalone-brand">Kestrel Ventures</p>

</main>
</body>
</html>
```